Flyer design for an e-recruitment software

I need a double sided brochure. The design should be clean and simple using our colours (see beta.hirnolux.example). I have attached the document outline for your consideration. This brochure will be used in both a conference (as a give away) and in subsequent briefing sessions. It must stand out in terms of the bold fonts, design aesthetics and look & feel.

Target Market(s)

Hiring managers, Human Resource leaders

Industry/Entity Type

Employment Agency

Font styles to use
Decorative

Colors
33a6d7
0555a3
ffffff

Requirements
Must have
• An image, good use of space, white colour helping to balance other colours (as shown on beta.hirnolux.example

```html
<!DOCTYPE html>
<html lang="en">
<head>
<meta charset="utf-8">
<title>Hirnolux – Recruitment Simplified</title>
<link href="https://fonts.googleapis.com/css2?family=Oswald:wght@400;500;600;700&family=Open+Sans:wght@400;600;700&display=swap" rel="stylesheet">
<style>
  :root {
    --sky: #33a6d7;
    --navy: #0555a3;
    --white: #ffffff;
    --ink: #1f2a36;
    --mist: #eef4f9;
    --photo-warm: #c9b8a6;
    --photo-cool: #9fb3c4;
  }
  * { margin: 0; padding: 0; box-sizing: border-box; }
  html, body { width: 900px; height: 1200px; overflow: hidden; background: var(--white); }
  .flyer { position: relative; width: 900px; height: 1200px; background: var(--white); overflow: hidden; font-family: "Open Sans", sans-serif; color: var(--ink); }

  .brand { position: absolute; left: 60px; top: 48px; }
  .brand-name { font-family: "Oswald", sans-serif; font-weight: 600; font-size: 78px; line-height: 1; color: var(--sky); letter-spacing: 1px; }
  .brand-tagline { font-size: 15px; color: var(--navy); margin-top: 6px; padding-left: 4px; }

  .headline-badge { position: absolute; right: 0; top: 0; width: 300px; height: 190px; background: var(--navy); display: flex; align-items: center; justify-content: center; }
  .headline-badge-inner { border: 3px solid var(--white); padding: 14px 22px; text-align: center; font-family: "Oswald", sans-serif; font-weight: 700; color: var(--white); font-size: 32px; line-height: 1.2; letter-spacing: 2px; }
  .headline-badge-inner hr { border: 0; border-top: 2px solid var(--white); margin: 6px 0; }

  .top-swoosh { position: absolute; left: 0; top: 170px; width: 900px; height: 110px; }

  .hero-photo { position: absolute; left: 0; top: 250px; width: 900px; height: 420px; background: linear-gradient(90deg, var(--white) 0%, var(--mist) 30%, var(--photo-cool) 55%, var(--photo-warm) 75%, #4a5563 100%); }

  .hero-copy { position: absolute; left: 60px; top: 330px; font-family: "Oswald", sans-serif; text-transform: uppercase; }
  .hero-copy .lead { font-size: 104px; font-weight: 700; color: var(--navy); line-height: 1; }
  .hero-copy .follow { font-size: 46px; font-weight: 500; color: var(--ink); line-height: 1.1; }

  .bottom-wave { position: absolute; left: 0; top: 610px; width: 900px; height: 140px; }

  .intro { position: absolute; left: 60px; right: 60px; top: 760px; text-align: center; font-size: 24px; font-weight: 600; line-height: 1.35; color: var(--ink); }
  .pivot { position: absolute; left: 0; right: 0; top: 840px; text-align: center; font-family: "Oswald", sans-serif; font-weight: 700; font-size: 58px; color: var(--navy); line-height: 1; }

  .questions { position: absolute; left: 70px; right: 70px; top: 912px; border: 3px solid var(--sky); border-radius: 6px; padding: 16px 30px; text-align: center; font-family: "Oswald", sans-serif; font-weight: 600; color: var(--navy); font-size: 30px; line-height: 1.3; background: var(--white); }
  .questions .dot { position: absolute; width: 22px; height: 22px; border-radius: 50%; border: 3px solid var(--sky); background: var(--white); bottom: -13px; }
  .questions .dot.left { left: -13px; }
  .questions .dot.right { right: -13px; }

  .footer { position: absolute; left: 0; bottom: 0; width: 900px; height: 110px; }
  .footer-band { position: absolute; inset: 0; }
  .footer-content { position: absolute; left: 40px; right: 40px; bottom: 24px; display: flex; align-items: flex-end; justify-content: space-between; color: var(--white); font-size: 15px; }
  .footer-cta { line-height: 1.35; font-weight: 600; }
  .contact { display: flex; gap: 40px; }
  .contact span { display: inline-flex; align-items: center; gap: 8px; }
  .contact svg { width: 16px; height: 16px; }
</style>
</head>
<body>
<div class="flyer">
  <div class="hero-photo" role="img" aria-label="Photo of a businesswoman sipping coffee at her desk beside a laptop in a bright office"></div>

  <svg class="top-swoosh" viewBox="0 0 900 110" preserveAspectRatio="none" aria-hidden="true">
    <path d="M0 40 C250 110 600 20 900 60 L900 110 L0 110 Z" fill="var(--white)"/>
    <path d="M0 30 C260 100 600 10 900 50 L900 62 C600 24 260 112 0 44 Z" fill="var(--sky)"/>
    <path d="M0 0 L900 0 L900 40 C600 5 260 90 0 20 Z" fill="var(--white)"/>
    <path d="M0 20 C260 90 600 5 900 40 L900 48 C600 14 260 98 0 30 Z" fill="var(--navy)"/>
  </svg>

  <div class="brand">
    <div class="brand-name">hirnolux</div>
    <div class="brand-tagline">Making hiring simple and fast</div>
  </div>

  <div class="headline-badge">
    <div class="headline-badge-inner">RECRUITMENT<hr>SIMPLIFIED</div>
  </div>

  <div class="hero-copy">
    <div class="lead">Investing</div>
    <div class="follow">In the right people</div>
    <div class="follow">is good business</div>
  </div>

  <svg class="bottom-wave" viewBox="0 0 900 140" preserveAspectRatio="none" aria-hidden="true">
    <path d="M0 50 C250 0 600 110 900 30 L900 140 L0 140 Z" fill="var(--white)"/>
    <path d="M0 40 C250 -10 600 100 900 20 L900 40 C600 115 250 10 0 58 Z" fill="var(--sky)"/>
    <path d="M0 62 C250 14 600 122 900 46 L900 56 C600 130 250 26 0 72 Z" fill="var(--navy)"/>
  </svg>

  <p class="intro">As an employer you want the best candidates to join you.<br>And a pool of talented candidates ready for the next opportunity</p>
  <div class="pivot">BUT</div>

  <div class="questions">
    Are you constrained by time in processing<br>
    far too many applications for the one job?<br>
    Are you spending too much money in the process?
    <span class="dot left"></span><span class="dot right"></span>
  </div>

  <footer class="footer">
    <svg class="footer-band" viewBox="0 0 900 110" preserveAspectRatio="none" aria-hidden="true">
      <path d="M0 30 C300 0 600 40 900 10 L900 110 L0 110 Z" fill="var(--sky)"/>
      <path d="M0 50 C300 20 600 60 900 30 L900 110 L0 110 Z" fill="var(--navy)" opacity="0.35"/>
    </svg>
    <div class="footer-content">
      <div class="footer-cta">Simplify your recruitment<br>Register with Hirnolux at</div>
      <div class="contact">
        <span><svg viewBox="0 0 16 16"><rect x="1" y="3" width="14" height="10" fill="none" stroke="#fff" stroke-width="1.5"/><path d="M1 3 L8 9 L15 3" fill="none" stroke="#fff" stroke-width="1.5"/></svg>hello.team@hirnolux.example</span>
        <span><svg viewBox="0 0 16 16"><circle cx="8" cy="8" r="6.5" fill="none" stroke="#fff" stroke-width="1.5"/><path d="M1.5 8 H14.5 M8 1.5 C4 5 4 11 8 14.5 M8 1.5 C12 5 12 11 8 14.5" fill="none" stroke="#fff" stroke-width="1.2"/></svg>www.hirnolux.example</span>
      </div>
    </div>
  </footer>
</div>
</body>
</html>
```